Computer Sales and Repairs business, 1/4 and 1/2 page advertisement

We need a 1/4 and 1/2 page advertisement for our business. We want to show what we do, contact information and brands that we are an authorised repair centre for.

Our current colour scheme is green and orange (as shown in the attached logo) however we are open to other colours that would stand out on a newspaper page.

We're looking for designs that aren't crowded/busy, not boxy, possibly a flat colour design.

For example computer/laptop images (if needed) we use the following pc cases and business class laptop such as:

http://q41752.shop.brelvanotech.example/OzStore/Items/Item.aspx?id=K7W81TR&opt=&sel=MKD
http://vortelplay.example/index_ss.php?id=603
http://vortelplay.example/index_ss.php?id=404

Dimensions for 1/4 page ad:

85mm D x 220mm W (allow for 15mm bleed area on bottom, left and right)

Industry/Entity Type

It Company

Font styles to use
Sans Serif

Colors

Designer to choose colors to be used in the design.

Requirements
Should not have
• Should not be crowded/busy or boxy

```html
<!DOCTYPE html>
<html lang="en">
<head>
<meta charset="utf-8">
<title>Circuit Menders — Advertisement</title>
<link rel="stylesheet" href="https://fonts.googleapis.com/css2?family=Open+Sans:wght@300;400;600;700;800&display=swap">
<style>
  :root {
    --orange: #f0821e;
    --green: #0c6a36;
    --grey-col: #d3d4d6;
    --panel: #f1f1f1;
    --ink: #141414;
    --white: #ffffff;
    --page: #f4f4f4;
    --case-dark: #1e2022;
    --case-mid: #4a4d50;
  }
  html, body {
    margin: 0;
    padding: 0;
    width: 975px;
    height: 1200px;
    overflow: hidden;
    background: var(--page);
    font-family: "Open Sans", Arial, sans-serif;
  }
  .canvas { position: relative; width: 975px; height: 1200px; }
  .ad {
    position: absolute;
    left: 20px; top: 269px;
    width: 935px; height: 662px;
    background: var(--panel);
    overflow: hidden;
    box-shadow: 4px 6px 10px rgba(0,0,0,0.25);
  }
  .top-band {
    position: absolute; left: 0; top: 0;
    width: 935px; height: 138px;
    background: var(--orange);
  }
  .right-edge {
    position: absolute; right: 0; top: 138px;
    width: 0; height: 0;
  }
  .brand-column {
    position: absolute; left: 0; top: 138px;
    width: 189px; height: 524px;
    background: var(--grey-col);
  }
  .content-panel {
    position: absolute; left: 189px; top: 138px;
    width: 746px; height: 466px;
    background: linear-gradient(135deg, #ececec 0%, #fafafa 100%);
  }
  .logo-box {
    position: absolute; left: 28px; top: 48px;
    width: 530px; height: 152px;
    background: var(--green);
    border: 5px solid var(--white);
    border-radius: 16px;
    box-sizing: border-box;
  }
  .logo-mark {
    position: absolute; left: 36px; top: 46px;
    width: 50px; height: 50px;
    border: 3px solid var(--white);
    box-sizing: border-box;
  }
  .logo-name {
    position: absolute; left: 162px; top: 22px;
    margin: 0;
    color: var(--white);
    font-weight: 700;
    font-size: 38px;
    line-height: 49px;
  }
  .contact {
    position: absolute; left: 570px; top: 56px;
    color: var(--white);
  }
  .contact-call {
    margin: 0;
    font-size: 27px;
    font-weight: 300;
    line-height: 34px;
  }
  .contact-call strong { font-weight: 700; }
  .contact-address {
    margin: 0;
    font-size: 17px;
    font-weight: 400;
  }
  .services-head {
    position: absolute; left: 189px; top: 219px;
    width: 470px; height: 46px;
    background: var(--orange);
  }
  .services-head h2 {
    margin: 0;
    padding-left: 30px;
    line-height: 46px;
    font-size: 33px;
    font-weight: 800;
    color: var(--ink);
  }
  .services {
    position: absolute; left: 219px; top: 280px;
    margin: 0; padding: 0;
    list-style: none;
    font-size: 22px;
    color: var(--ink);
    line-height: 25px;
  }
  .services li { margin-bottom: 17px; }
  .services li.two-line { line-height: 24px; }
  .product-backdrop {
    position: absolute; left: 600px; top: 208px;
    width: 340px; height: 395px;
  }
  .product-photo {
    position: absolute; left: 636px; top: 186px;
    width: 275px; height: 422px;
    border-radius: 10px 10px 4px 4px;
    background: linear-gradient(160deg, var(--case-mid) 0%, var(--case-dark) 55%, #0d0e0f 100%);
  }
  .brands {
    position: absolute; left: 0; top: 214px;
    width: 189px;
    margin: 0; padding: 0;
    list-style: none;
    text-align: center;
    font-weight: 700;
    font-size: 23px;
    color: #1f4fa0;
  }
  .brands li { height: 55px; line-height: 55px; }
  .footer {
    position: absolute; left: 189px; top: 604px;
    width: 746px; height: 58px;
    background: var(--ink);
    color: var(--white);
    text-align: center;
    font-size: 25px;
    line-height: 52px;
  }
</style>
</head>
<body>
<div class="canvas">
  <section class="ad">
    <div class="top-band"></div>
    <div class="brand-column"></div>
    <div class="content-panel"></div>

    <div class="logo-box">
      <div class="logo-mark"></div>
      <h1 class="logo-name">Circuit<br>Menders</h1>
    </div>

    <div class="contact">
      <p class="contact-call">CALL US: <strong>(02) 5550 1938</strong></p>
      <p class="contact-address">87B Harbour Lane, Wexbury, NSW, 2999</p>
    </div>

    <div class="services-head"><h2>What we do:</h2></div>
    <ul class="services">
      <li>New Computers and Laptops</li>
      <li>Computer and Laptop Repairs</li>
      <li class="two-line">Fixed Price Computer and Network<br>Complete Management</li>
      <li>Backup and Virus Protection</li>
      <li>Internet Services</li>
      <li>Printer Sales and Repairs</li>
      <li>Data Recovery</li>
    </ul>

    <svg class="product-backdrop" viewBox="0 0 340 395" aria-hidden="true">
      <path d="M60 60 Q70 30 100 30 L300 30 Q330 30 335 60 L340 395 L0 395 L0 300 Q0 270 20 250 Z" fill="#f0821e"/>
    </svg>
    <div class="product-photo" role="img" aria-label="Photo of a black Vortel desktop PC tower case with front ports and a honeycomb mesh front panel"></div>

    <ul class="brands">
      <li>Brelvano</li>
      <li>Tarrek</li>
      <li>Dorvix</li>
      <li>Ipsara</li>
      <li>Lumerak</li>
      <li>Netlyx</li>
      <li>Powren</li>
      <li>Kyoren Ofis</li>
    </ul>

    <div class="footer">circuitmenders.example</div>
  </section>
</div>
</body>
</html>
```